Kinsmen Crest Beard Oil Label for 1oz dropper bottle

Create a label for a 1oz beard oil dropper bottle. The label is 1.5 inches tall and 2.75 inches wide. Our logo is listed in the brief so please use it but it doesnt have to be that prominent. BEARD OIL is the most important verbiage. We like elements of all the attached images but we want our own look and feel.

Target Market(s)

Men with beards

Requirements
Must have
• Kinsmen Crest Logo, BEARD OIL, Flavor (Tobacco Vanilla)

Ingredients
Fractionated Coconut Oil (MCT)
Golden Jojoba Oil
Hemp Seed Oil
Tea Tree Essential Oil
Orange Bitter Essential Oil
Peppermint Supreme Essential Oil
Tallow Aromas
DYE FREE

Directions:
Directions: apply 3-6 drops into your hand...rub oil into hands and apply directly onto beard. For best results massage into skin under beard area and work oil out towards beard. Discontinue use if skin becomes irritated.

100% MADE IN THE USA (American Flag 1 color)
Veteran Owned Co.
Nice to have
• Labels can change color with each flavor or a ring can change color to show flavor.

```html
<!DOCTYPE html>
<html lang="en">
<head>
<meta charset="utf-8">
<title>Kinsmen Crest Beard Oil Label</title>
<link rel="stylesheet" href="https://fonts.googleapis.com/css2?family=Alfa+Slab+One&family=Rye&display=swap">
<style>
  :root {
    --page-bg: #a3a3a3;
    --panel-grey: #dcdcdc;
    --panel-grey-dark: #c9c9c9;
    --label-white: #f4f4f4;
    --ink: #1c1c1c;
    --brand-red: #c8202a;
    --paper: #ffffff;
  }
  * { box-sizing: border-box; margin: 0; padding: 0; }
  html, body { width: 848px; height: 1200px; overflow: hidden; }
  body {
    background: var(--page-bg);
    font-family: "Alfa Slab One", Georgia, serif;
    color: var(--ink);
    position: relative;
  }
  .label {
    position: absolute;
    left: 44px; top: 392px;
    width: 760px; height: 416px;
    background: var(--label-white);
    box-shadow: 0 6px 14px rgba(0,0,0,0.25);
    overflow: hidden;
  }
  .panel { position: absolute; top: 0; height: 100%; }
  .panel--ingredients {
    left: 0; width: 188px;
    background: linear-gradient(180deg, var(--panel-grey), var(--panel-grey-dark));
  }
  .panel--front {
    left: 188px; width: 382px;
    background: radial-gradient(circle at 50% 55%, #ffffff 0%, #ececec 55%, #d6d6d6 100%);
  }
  .panel--directions {
    left: 570px; width: 190px;
    background: linear-gradient(180deg, var(--panel-grey), var(--panel-grey-dark));
  }
  .ingredients-list {
    position: absolute; left: 14px; right: 14px; top: 30px;
    text-align: center; text-transform: uppercase;
    font-size: 11.5px; line-height: 15.5px; letter-spacing: 0.3px;
  }
  .brand-block {
    position: absolute; left: 0; bottom: 0; width: 100%; height: 110px;
    background: var(--ink);
    display: flex; align-items: center; justify-content: center;
  }
  .brand-name {
    font-family: "Alfa Slab One", Georgia, serif;
    text-transform: uppercase; text-align: center;
    line-height: 1;
  }
  .brand-block .brand-name { color: var(--paper); font-size: 21px; }
  .front-brand {
    position: absolute; top: 22px; left: 0; width: 100%;
    color: var(--ink); font-size: 27px;
  }
  .product-title {
    position: absolute; top: 76px; left: 0; width: 100%;
    text-align: center;
    font-family: "Rye", Georgia, serif;
    font-size: 56px; line-height: 1;
    color: var(--brand-red);
    letter-spacing: 1px;
  }
  .portrait {
    position: absolute; left: 118px; top: 150px;
    width: 146px; height: 146px; border-radius: 50%;
    background: radial-gradient(circle at 45% 40%, #7a7a7a 0%, #3a3a3a 65%, #1c1c1c 100%);
    border: 4px solid var(--ink);
  }
  .flavor-band {
    position: absolute; left: 62px; top: 304px;
    width: 258px; height: 34px;
    background: var(--brand-red);
    outline: 2px solid var(--ink); outline-offset: 2px;
    color: var(--paper);
    font-size: 16px; letter-spacing: 1px;
    display: flex; align-items: center; justify-content: center;
    text-transform: uppercase;
  }
  .directions {
    position: absolute; left: 12px; right: 12px; top: 30px;
    text-align: center; text-transform: uppercase;
    font-size: 10px; line-height: 13px;
  }
  .directions p + p { margin-top: 12px; }
  .veteran-badge {
    position: absolute; left: 50px; top: 238px;
    width: 90px; height: 56px;
  }
  .made-in {
    position: absolute; left: 0; width: 100%; top: 318px;
    text-align: center; font-size: 9.5px; text-transform: uppercase;
  }
</style>
</head>
<body>
  <section class="label" aria-label="Kinsmen Crest beard oil label">
    <div class="panel panel--ingredients">
      <p class="ingredients-list">Ingredients:<br>Fractionated coconut oil (MCT), golden jojoba oil, hemp seed oil, tea tree essential oil, orange bitter essential oil, peppermint supreme essential oil, Tallow Aromas, dye free</p>
      <div class="brand-block"><p class="brand-name">Kinsmen<br>Crest</p></div>
    </div>

    <div class="panel panel--front">
      <p class="brand-name front-brand">Kinsmen Crest</p>
      <h1 class="product-title">BEARD OIL</h1>
      <div class="portrait" role="img" aria-label="Illustrated bearded man in profile inside a circle"></div>
      <p class="flavor-band">Tobacco Vanilla</p>
    </div>

    <div class="panel panel--directions">
      <div class="directions">
        <p>- Directions -<br>Apply 3-6 drops into your hand. Rub oil into hands and apply directly onto beard. For best results massage into skin under beard area and work oil out towards beard.</p>
        <p>Discontinue use if skin becomes irritated.</p>
      </div>
      <svg class="veteran-badge" viewBox="0 0 90 56" aria-hidden="true">
        <ellipse cx="45" cy="28" rx="40" ry="24" fill="#ffffff" stroke="#2b4f8f" stroke-width="3"/>
        <rect x="8" y="22" width="74" height="12" fill="#c8202a"/>
      </svg>
      <p class="made-in">100% Made in the USA</p>
    </div>
  </section>
</body>
</html>
```